VORK.
BRIDGING HORIZONS
VORK. -
Creative Brief
Use specific fonts
any thing which suits with the LOGO provided
Professional
RAJESH MOTLA
MR.
B.P. No.6213, COMMUNE-3, NEAR TORAVI LAUNDRY, KALEBA ZONE, BAMAKO-MALI
rajesh@vork.co.in
vork.co.in
pls mention MANAGING DIRECTOR, the designation, below the name of the person.
LOGO at centre. Below mentioned address at bottom: India Office D-47, Palm Enclave-II, Gurgaon, Haryana 122015 ph:+91-124-4708352, fax:+91-124-4519267 cell:+91-9871436029

```html
<!DOCTYPE html>
<html lang="en">
<head>
<meta charset="utf-8">
<title>VORK. Business Cards</title>
<link href="https://fonts.googleapis.com/css2?family=Arimo:ital,wght@0,400;0,700;1,400;1,700&display=swap" rel="stylesheet">
<style>
  :root{
    --bg:#e9e6e1;
    --card:#ffffff;
    --navy:#0f2f6b;
    --blue:#1f5fae;
    --teal:#2a9bc4;
    --green:#6aa82a;
    --grey:#555b63;
    --rule:#c9ccd1;
  }
  *{box-sizing:border-box;margin:0;padding:0}
  html,body{width:1200px;height:852px;overflow:hidden}
  body{background:var(--bg);position:relative;font-family:"Arimo",Arial,sans-serif}
  .card{position:absolute;width:580px;height:340px;background:var(--card);border-radius:22px;overflow:hidden;box-shadow:0 6px 18px rgba(0,0,0,.18)}
  .card--left{left:70px;top:70px}
  .card--right{left:550px;top:442px}
  .card__band{position:absolute;left:0;top:0;bottom:0;width:26px;background:linear-gradient(180deg,var(--teal),var(--blue) 45%,var(--navy))}
  .card__band::after{content:"";position:absolute;right:-5px;top:0;bottom:0;width:4px;background:var(--green)}
  .brand{display:flex;align-items:center;gap:10px}
  .brand__dot{width:58px;height:58px;border-radius:50%;background:var(--blue);flex:none}
  .brand__name{font-weight:700;font-size:54px;color:var(--blue);letter-spacing:2px;line-height:1}
  .brand__tag{font-weight:700;font-size:13px;color:var(--green);letter-spacing:1.5px;margin-top:4px}
  .person__name{font-weight:700;font-size:21px;color:var(--navy)}
  .person__title{font-style:italic;font-weight:700;font-size:15px;color:var(--green);margin-top:3px}
  .address{font-size:14px;line-height:1.45;color:var(--grey)}
  .contacts{list-style:none;font-size:14px;color:var(--grey)}
  .contacts li{display:flex;align-items:center;gap:9px;height:22px}
  .contacts svg{width:15px;height:15px;flex:none}
  .divider{position:absolute;width:1px;background:var(--rule)}
  /* left card */
  .card--left .brand-block{position:absolute;left:60px;top:120px}
  .card--left .divider{left:290px;top:40px;height:260px}
  .card--left .details{position:absolute;left:312px;top:48px;width:250px}
  .card--left .address{margin-top:10px}
  .card--left .contacts{margin-top:22px}
  /* right card */
  .card--right .brand-block{position:absolute;left:140px;top:34px}
  .card--right .person{position:absolute;left:100px;top:146px;width:210px;text-align:right}
  .card--right .address{margin-top:12px}
  .card--right .divider{left:326px;top:150px;height:150px}
  .card--right .contacts{position:absolute;left:346px;top:160px}
</style>
</head>
<body>

<svg width="0" height="0" style="position:absolute" aria-hidden="true">
  <defs>
    <symbol id="i-phone" viewBox="0 0 16 16"><path d="M4 1h3l1 4-2 1a8 8 0 0 0 4 4l1-2 4 1v3a2 2 0 0 1-2 2A12 12 0 0 1 1 3a2 2 0 0 1 2-2z" fill="#1f5fae"/></symbol>
    <symbol id="i-mobile" viewBox="0 0 16 16"><rect x="4" y="1" width="8" height="14" rx="1.5" fill="#1f5fae"/><rect x="5.5" y="3" width="5" height="8" fill="#fff"/></symbol>
    <symbol id="i-mail" viewBox="0 0 16 16"><circle cx="8" cy="8" r="7" fill="#1f5fae"/><text x="8" y="11.5" text-anchor="middle" font-size="10" font-family="Arial" fill="#fff">@</text></symbol>
    <symbol id="i-web" viewBox="0 0 16 16"><circle cx="8" cy="8" r="7" fill="#1f5fae"/><path d="M1 8h14M8 1c-3 3-3 11 0 14M8 1c3 3 3 11 0 14" stroke="#fff" fill="none" stroke-width="1"/></symbol>
  </defs>
</svg>

<article class="card card--left">
  <div class="card__band"></div>
  <div class="brand-block">
    <div class="brand"><span class="brand__dot"></span><span class="brand__name">VORK</span></div>
    <div class="brand__tag">BRIDGING HORIZONS</div>
  </div>
  <div class="divider"></div>
  <div class="details">
    <div class="person__name">Rajesh Motla</div>
    <div class="person__title">Managing Director</div>
    <p class="address">B.P. No.6213, Commune-3,<br>Near Toravi Laundry,<br>Kaleba Zone, Bamako-Mali</p>
    <ul class="contacts">
      <li><svg><use href="#i-phone"/></svg>+223-20418836</li>
      <li><svg><use href="#i-mobile"/></svg>+223-76341902</li>
      <li><svg><use href="#i-mail"/></svg>rajesh@vork.co.in</li>
      <li><svg><use href="#i-web"/></svg>www.vork.co.in</li>
    </ul>
  </div>
</article>

<article class="card card--right">
  <div class="card__band"></div>
  <div class="brand-block">
    <div class="brand"><span class="brand__dot"></span><span class="brand__name">VORK</span></div>
    <div class="brand__tag" style="margin-left:68px">BRIDGING HORIZONS</div>
  </div>
  <div class="person">
    <div class="person__name">Rajesh Motla</div>
    <div class="person__title">Managing Director</div>
    <p class="address">B.P. No.6213, Commune-3,<br>Near Toravi Laundry,<br>Kaleba Zone, Bamako-Mali</p>
  </div>
  <div class="divider"></div>
  <ul class="contacts">
    <li><svg><use href="#i-phone"/></svg>+223-20418836</li>
    <li><svg><use href="#i-mobile"/></svg>+223-76341902</li>
    <li><svg><use href="#i-mail"/></svg>rajesh@vork.co.in</li>
    <li><svg><use href="#i-web"/></svg>www.vork.co.in</li>
  </ul>
</article>

</body>
</html>
```